Business Card Design using new attached logo

We are a family run Plumbing and Heating firm looking to improve our company image with an improved business card and new logo.We are looking to keep the company colour (Blue) involved in our design

Reason: New logo added which needs to be incorporated on designs

Industry/Entity Type

Business

Contact Information for Business Card

See attachment of all info required.

Requirements
Must have
• We have just picked a new company logo which is attached.
• Could you please provide your business card designs using this logo.
• We are looking for the logo on the back as well as the front with all the info required

```html
<!DOCTYPE html>
<html lang="en">
<head>
<meta charset="utf-8">
<title>Kestrel Heating Ltd – Business Cards</title>
<link rel="stylesheet" href="https://fonts.googleapis.com/css2?family=Cinzel:wght@400;700&family=Open+Sans:wght@400;700&display=swap">
<style>
  :root {
    --stage: #e6e6e6;
    --brand-blue: #1f43d6;
    --brand-blue-deep: #0c2496;
    --brand-blue-light: #3a5ff0;
    --ink: #2b2b2b;
    --paper: #ffffff;
    --paper-shade: #f1f1f1;
  }
  * { box-sizing: border-box; margin: 0; padding: 0; }
  html, body { width: 1200px; height: 871px; overflow: hidden; }
  body { background: var(--stage); position: relative; font-family: "Open Sans", sans-serif; }

  .card {
    position: absolute;
    left: 300px;
    width: 600px;
    height: 353px;
    border-radius: 3px;
    box-shadow: 0 6px 18px rgba(0,0,0,0.18);
    overflow: hidden;
  }

  /* Back of card */
  .card-back {
    top: 62px;
    background: linear-gradient(160deg, var(--brand-blue-light) 0%, var(--brand-blue) 45%, var(--brand-blue-deep) 100%);
  }
  .card-back .wordmark {
    position: absolute;
    left: 0; right: 0; top: 50%;
    transform: translateY(-50%);
    display: flex; align-items: center; justify-content: center; gap: 14px;
  }
  .card-back .mark-square { width: 40px; height: 40px; background: var(--paper); }
  .card-back .brand-name {
    font-family: "Cinzel", serif; font-weight: 400; font-size: 30px;
    letter-spacing: 2px; color: var(--paper);
  }

  /* Front of card */
  .card-front {
    top: 456px;
    background: linear-gradient(180deg, var(--paper) 0%, var(--paper-shade) 100%);
  }
  .card-front .edge-band {
    position: absolute; left: 0; right: 0; bottom: 0; height: 16px;
    background: var(--brand-blue);
  }
  .card-front .wordmark {
    position: absolute; left: 200px; top: 34px;
    display: flex; align-items: center; gap: 12px;
  }
  .card-front .mark-square { width: 34px; height: 34px; background: var(--brand-blue); }
  .card-front .brand-name {
    font-family: "Cinzel", serif; font-weight: 400; font-size: 24px;
    letter-spacing: 1.5px; color: var(--brand-blue);
  }
  .holder { position: absolute; left: 48px; top: 112px; }
  .holder-name {
    font-family: "Cinzel", serif; font-weight: 700; font-size: 18px;
    color: var(--ink); letter-spacing: 1px;
  }
  .holder-role {
    font-family: "Cinzel", serif; font-size: 15px;
    color: var(--brand-blue); letter-spacing: 1px; margin-top: 2px;
  }
  .contact { position: absolute; left: 330px; top: 136px; font-size: 12px; color: var(--ink); line-height: 1.55; }
  .contact .company { font-weight: 700; color: var(--brand-blue); font-size: 11.5px; }
  .contact .address { margin-bottom: 10px; }
  .contact-list { list-style: none; }
  .contact-list li { display: flex; align-items: center; gap: 12px; height: 21px; }
  .contact-list svg { width: 13px; height: 13px; flex: none; fill: none; stroke: var(--brand-blue); stroke-width: 1.6; }
</style>
</head>
<body>

<section class="card card-back" aria-label="Card back">
  <div class="wordmark">
    <span class="mark-square"></span>
    <span class="brand-name">KESTREL HEATING LTD</span>
  </div>
</section>

<section class="card card-front" aria-label="Card front">
  <div class="wordmark">
    <span class="mark-square"></span>
    <span class="brand-name">KESTREL HEATING LTD</span>
  </div>

  <div class="holder">
    <p class="holder-name">Daniel Morrow</p>
    <p class="holder-role">Director</p>
  </div>

  <div class="contact">
    <p class="company">KESTREL HEATING LTD</p>
    <p class="address">14 Mill Lane<br>harbour road, ashford, kent</p>
    <ul class="contact-list">
      <li>
        <svg viewBox="0 0 16 16" aria-hidden="true"><path d="M2 5c0-2 2-3 6-3s6 1 6 3l-3 1-1-2H6L5 6zM4 8h8l1 6H3z"/></svg>
        <span>020 7946 0321</span>
      </li>
      <li>
        <svg viewBox="0 0 16 16" aria-hidden="true"><rect x="4" y="1.5" width="8" height="4"/><rect x="1.5" y="5.5" width="13" height="6"/><rect x="4" y="9.5" width="8" height="5"/></svg>
        <span>020 7946 0458</span>
      </li>
      <li>
        <svg viewBox="0 0 16 16" aria-hidden="true"><rect x="4.5" y="1.5" width="7" height="13" rx="1"/><path d="M7 12.5h2"/></svg>
        <span>07700 900274</span>
      </li>
      <li>
        <svg viewBox="0 0 16 16" aria-hidden="true"><rect x="1.5" y="3.5" width="13" height="9"/><path d="M1.5 3.5 8 9l6.5-5.5"/></svg>
        <span>danielmorrow@kestrelheating.co.uk</span>
      </li>
    </ul>
  </div>

  <div class="edge-band"></div>
</section>

</body>
</html>
```